Tree Pruning Website

We need a website for a tree Arborist, pruning company called Hollow Ridge Branchworks. We look after all types of trees, knock down trees and prune trees. Our target market is from domestic clients to government clients and everything in between.

We would like to see the use of our main colours which are orange and green

We are not looking forward in seeing a template that we have seen before but a unique template. We have designed 5 templates ourselves and we wish for the design community to take our designs to the next level.

We have also designed a template for things that **we are not** looking for (Version 4)

To make it fair for everyone, we are also not giving out any participation payments as we have had. One winner will take all of the payment!!!

I Have attached a image of the designs and a image of a tree.

We are just looking at the PSD file been developed. We have our own team who can slice the image up into a HTML format.

Target Market(s)

Everyone who needs to cut down a tree

Industry/Entity Type

Government

Requirements
Must have
• Logo on front page
A List of our services
jQuery slider on page
Phone Number on every page

```html
<!DOCTYPE html>
<html lang="en">
<head>
<meta charset="utf-8">
<title>Hollow Ridge Branchworks</title>
<link href="https://fonts.googleapis.com/css2?family=Open+Sans:wght@400;600;700&family=Noto+Serif:wght@400&family=Oswald:wght@300;400&display=swap" rel="stylesheet">
<style>
:root{
  --olive:#6f7b0b;
  --lime:#a7c11c;
  --logo:#c7dc3a;
  --orange:#f0a800;
  --orange-deep:#d98f00;
  --dark-green:#3d4a05;
  --ink:#333333;
  --muted:#666666;
  --band:#eeeef2;
  --card:#eeeef0;
  --footer:#3b3b3b;
  --footer-deep:#2c2c2c;
  --footer-text:#8a8a8a;
  --white:#ffffff;
}
*{margin:0;padding:0;box-sizing:border-box}
html,body{width:1065px;height:1200px;overflow:hidden}
body{position:relative;background:var(--white);font-family:"Open Sans",Arial,sans-serif;color:var(--ink)}
.abs{position:absolute}

.hero-band{left:0;top:0;width:1065px;height:378px;background:var(--olive)}
.brand{left:272px;top:18px;display:flex;align-items:center;gap:8px}
.brand-dot{width:62px;height:62px;border-radius:50%;background:var(--logo)}
.brand-name{font-family:"Open Sans",sans-serif;font-weight:700;font-size:17px;line-height:19px;color:var(--logo)}

.main-nav{left:479px;top:78px;display:flex;align-items:center;font-size:8.5px;color:var(--white)}
.main-nav a{color:var(--white);text-decoration:none;margin-right:19px}
.main-nav .current{position:relative;background:var(--orange);padding:5px 9px;border-radius:3px;margin-right:9px}
.main-nav .current::after{content:"";position:absolute;left:50%;bottom:-4px;margin-left:-4px;border:4px solid transparent;border-bottom:0;border-top-color:var(--orange)}

.slider{left:272px;top:114px;width:521px;height:264px;border:2px solid var(--orange);background:linear-gradient(180deg,#9bb6c9 0%,#7c8a3a 35%,#8a5a2e 70%,#6b3f1f 100%)}
.slider-arrow{top:209px;width:29px;height:29px;border:2px solid var(--orange);border-radius:50%;display:flex;align-items:center;justify-content:center}
.slider-arrow.prev{left:233px}
.slider-arrow.next{left:805px}

.intro-bar{left:272px;top:377px;width:521px;height:69px;background:var(--orange);box-shadow:0 14px 14px -10px rgba(0,0,0,.28)}
.intro-text{left:10px;top:10px;width:340px;font-size:12.4px;line-height:16px;color:var(--white);font-weight:400}
.intro-text strong{color:var(--dark-green);font-weight:700}
.phone-box{left:349px;top:0;width:172px;height:69px;background:linear-gradient(90deg,var(--orange-deep),var(--orange));display:flex;align-items:center;padding-left:12px;gap:10px}
.phone-ring{width:35px;height:35px;border-radius:50%;background:var(--dark-green);border:3px solid var(--logo);display:flex;align-items:center;justify-content:center}
.phone-number{font-family:"Oswald",sans-serif;font-weight:300;font-size:21px;color:var(--white)}

.feature{top:502px;width:122px;text-align:center}
.feature-icon{width:38px;height:38px;margin:0 auto;border-radius:50%;background:var(--dark-green);border:3px solid var(--orange);display:flex;align-items:center;justify-content:center}
.feature h3{margin-top:13px;font-size:10px;font-weight:700;color:var(--ink)}
.feature p{margin-top:12px;font-size:7.4px;line-height:11.6px;color:var(--muted)}
.btn{display:inline-block;background:var(--orange);color:var(--white);font-size:7.8px;font-weight:600;padding:5px 4px;border-radius:2px;text-decoration:none}
.feature .btn{margin-top:11px}

.section-head{top:698px;height:34px;border-top:1px solid #e2e2e2}
.section-head h2{font-family:"Noto Serif",serif;font-weight:400;font-size:13px;color:var(--ink);margin-top:6px}
.section-head .rule{position:absolute;left:0;bottom:0;width:100%;height:5px;background:var(--lime)}
.section-head .rule::after{content:"";position:absolute;left:0;top:5px;border-top:7px solid var(--lime);border-right:7px solid transparent}
.pager{position:absolute;right:0;top:8px;display:flex;gap:3px}
.pager span{width:14px;height:14px;border:1px solid #d6d6d6;border-radius:50%}

.work-card{top:753px;width:121px;height:130px;background:var(--card)}
.work-photo{height:88px;border:2px solid var(--orange);position:relative}
.work-photo::after{content:"";position:absolute;left:-2px;bottom:-9px;border-top:7px solid var(--lime);border-right:7px solid transparent}
.work-card h4{font-family:"Noto Serif",serif;font-weight:400;font-size:9px;color:var(--ink);margin:9px 0 0 5px}
.work-card small{display:block;font-family:"Noto Serif",serif;font-size:6.8px;color:#888;margin-left:5px}

.quote-box{left:672px;top:754px;width:121px;height:89px;border:1px solid #d9d9d9;background:#f7f7f9;padding:10px 8px;font-size:6.9px;line-height:10px;font-style:italic;color:#888}
.quote-box::after{content:"";position:absolute;left:15px;bottom:-13px;border-top:13px solid #d9d9d9;border-right:13px solid transparent}
.quote-author{left:690px;top:867px;display:flex;align-items:center;gap:8px;font-size:7.5px;color:var(--ink)}
.quote-author b{font-weight:700}

.tweet-band{left:0;top:916px;width:1065px;height:57px;background:var(--band)}
.tweet-mark{left:288px;top:13px;width:30px;height:30px;border-radius:50%;background:#555}
.tweet-text{left:347px;top:12px;font-size:9px;line-height:12px;color:var(--ink)}
.tweet-text .link{color:#8aa000}

.site-footer{left:0;top:973px;width:1065px;height:201px;background:var(--footer)}
.footer-col{top:24px}
.footer-col h5{font-family:"Noto Serif",serif;font-weight:400;font-size:9.3px;color:var(--white);margin-bottom:11px}
.footer-col p{font-size:6.3px;line-height:10px;color:var(--footer-text)}
.news-item{border-bottom:1px solid #4d4d4d;padding:0 0 6px;margin-bottom:8px;width:110px}
.news-item.lead{color:#c8d400}
.gallery{display:grid;grid-template-columns:repeat(3,32px);column-gap:13px;row-gap:15px}
.gallery span{width:32px;height:29px;border:1px solid #ccc}
.map-area{width:119px;height:62px;border:1px solid #ccc;background:linear-gradient(135deg,#e6e2d6,#d6e2c4)}
.contact-line{display:flex;align-items:center;gap:7px;font-size:6.3px;color:#cfcfcf;margin-top:5px}
.contact-line i{display:inline-block;width:8px;height:6px;background:#888}

.base-bar{left:0;top:1174px;width:1065px;height:26px;background:var(--footer-deep)}
.base-bar p{position:absolute;left:272px;top:8px;font-size:6.3px;color:#999}
.social{position:absolute;left:745px;top:8px;display:flex;gap:10px}
.social span{width:9px;height:9px;background:#8c8c8c}
</style>
</head>
<body>

<div class="abs hero-band"></div>

<div class="abs brand">
  <span class="brand-dot"></span>
  <span class="brand-name">Hollow Ridge<br>Branchworks</span>
</div>

<nav class="abs main-nav">
  <a class="current" href="#">Home</a>
  <a href="#">About Us</a>
  <a href="#">Our Services</a>
  <a href="#">Get A quote</a>
  <a href="#">Our Work</a>
  <a href="#">Contact Us</a>
</nav>

<div class="abs slider" role="img" aria-label="Slider photo looking up the trunk of a large tree into its leafy canopy"></div>
<div class="abs slider-arrow prev"><svg width="14" height="12" viewBox="0 0 14 12"><path d="M13 6H2M6 1L1 6l5 5" fill="none" stroke="#f0a800" stroke-width="2"/></svg></div>
<div class="abs slider-arrow next"><svg width="14" height="12" viewBox="0 0 14 12"><path d="M1 6h11M8 1l5 5-5 5" fill="none" stroke="#f0a800" stroke-width="2"/></svg></div>

<div class="abs intro-bar">
  <p class="abs intro-text">Hollow Ridge Branchworks is the leading tree pruning services located Perth. Our motto is when you call, we <strong>guarantee</strong> to turn up and <strong>provide care</strong> to our customers.</p>
  <div class="abs phone-box">
    <span class="phone-ring"><svg width="15" height="15" viewBox="0 0 24 24"><path d="M6.6 10.8a15 15 0 0 0 6.6 6.6l2.2-2.2c.3-.3.7-.4 1-.2 1.1.4 2.3.6 3.6.6.6 0 1 .4 1 1V20c0 .6-.4 1-1 1A17 17 0 0 1 3 4c0-.6.4-1 1-1h3.5c.6 0 1 .4 1 1 0 1.3.2 2.5.6 3.6.1.3 0 .7-.2 1z" fill="#fff"/></svg></span>
    <span class="phone-number">08 5550 1420</span>
  </div>
</div>

<section class="abs feature" style="left:272px">
  <div class="feature-icon"><svg width="14" height="16" viewBox="0 0 14 16"><rect x="2" y="4" width="10" height="11" rx="2" fill="#fff"/><rect x="5" y="1" width="4" height="4" fill="none" stroke="#fff" stroke-width="1.5"/></svg></div>
  <h3>DOMESTIC</h3>
  <p>At vero eos et accusam et justo duo dolores et ea rebum. Stet clita kasd gubergren, no sea takimata sanctus est Lorem ipsum dolor sit amet.</p>
  <a class="btn" href="#">Learn more</a>
</section>
<section class="abs feature" style="left:404px">
  <div class="feature-icon"><svg width="18" height="12" viewBox="0 0 18 12"><path d="M1 1h7v10H1zM10 1h7v10h-7z" fill="#fff"/></svg></div>
  <h3>COMMERCIAL</h3>
  <p>Ut wisi enim ad minim veniam, quis nostrud exerci tation ullamcorper suscipit lobortis nisl ut aliquip ex ea commodo consequat.</p>
  <a class="btn" href="#">Learn more</a>
</section>
<section class="abs feature" style="left:538px">
  <div class="feature-icon"><svg width="16" height="16" viewBox="0 0 16 16"><circle cx="8" cy="5" r="4" fill="#fff"/><path d="M1 16c0-4 3-6 7-6s7 2 7 6z" fill="#fff"/></svg></div>
  <h3>GOVERMENT</h3>
  <p>Nam liber tempor cum soluta nobis eleifend option congue nihil imperdiet doming id quod mazim placerat facer possim assum.</p>
  <a class="btn" href="#">Learn more</a>
</section>
<section class="abs feature" style="left:671px">
  <div class="feature-icon"><svg width="16" height="16" viewBox="0 0 16 16"><path d="M2 14C2 6 7 2 14 2c0 7-4 12-12 12z" fill="#fff"/><path d="M3 13l8-8" stroke="#3d4a05" stroke-width="1.2"/></svg></div>
  <h3>NON PROFIT</h3>
  <p>Lorem ipsum dolor sit amet, consetetur sadipscing elitr, sed diam nonumy eirmod tempor invidunt ut labore et dolore.</p>
  <a class="btn" href="#">Learn more</a>
</section>

<div class="abs section-head" style="left:272px;width:388px">
  <h2>Our Services</h2>
  <div class="pager"><span></span><span></span></div>
  <div class="rule"></div>
</div>
<div class="abs section-head" style="left:672px;width:121px">
  <h2>&nbsp;Testimonials</h2>
  <div class="pager"><span></span><span></span></div>
  <div class="rule"></div>
</div>

<article class="abs work-card" style="left:272px">
  <div class="work-photo" role="img" aria-label="Photo of pale gum tree trunks against the sky" style="background:linear-gradient(160deg,#8fa3b8,#c9c4b4 55%,#6e6a4a)"></div>
  <h4>Observation 1</h4><small>Locations</small>
</article>
<article class="abs work-card" style="left:405px">
  <div class="work-photo" role="img" aria-label="Photo of a dark tree canopy with bright green leaves" style="background:linear-gradient(160deg,#6fa62c,#2c3a14 55%,#8fbf3c)"></div>
  <h4>Observation 1</h4><small>Locations</small>
</article>
<article class="abs work-card" style="left:538px">
  <div class="work-photo" role="img" aria-label="Photo of a sunlit path through a green forest" style="background:radial-gradient(circle at 55% 55%,#e4d99a,#6f8a2a 45%,#2f4514)"></div>
  <h4>Observation 1</h4><small>Locations</small>
</article>

<blockquote class="abs quote-box">" Duis autem vel eum iriure dolor in hendrerit in feugiat nulla facilisis at vero eros et accumsan vulputate velit esse molestie consequat, vel illum dolore eu pasto. "</blockquote>
<div class="abs quote-author">
  <svg width="13" height="13" viewBox="0 0 16 16"><circle cx="8" cy="5" r="4" fill="#444"/><path d="M1 16c0-4 3-6 7-6s7 2 7 6z" fill="#444"/></svg>
  <span><b>Mara Kettle</b> - Goverment -</span>
</div>

<div class="abs tweet-band">
  <span class="abs tweet-mark"></span>
  <p class="abs tweet-text"><span class="link">@hollowridgebw</span> Stet clita kasd gubergren, no sea takimata sanctus est Lorem ipsum....by <span class="link">hollowridgebw</span><br>about 2 hour ago</p>
</div>

<footer class="abs site-footer">
  <div class="abs footer-col" style="left:272px;width:115px">
    <h5>ABOUT US</h5>
    <p>Hollow Ridge Branchworks cares for trees of every size across the metro area. Our crews prune, shape and remove trees safely for homes, businesses and councils, and we clean up every site before we leave.</p>
  </div>
  <div class="abs footer-col" style="left:405px">
    <h5>LATEST NEWS</h5>
    <p class="news-item">Winter pruning bookings now open for the season.</p>
    <p class="news-item lead">Storm damage crews on call.</p>
    <p class="news-item">New chipper added to our fleet this month.</p>
    <p class="news-item">Free quotes for council and school grounds.</p>
  </div>
  <div class="abs footer-col" style="left:539px">
    <h5>GALLERY</h5>
    <div class="gallery">
      <span role="img" aria-label="Gallery photo of a water drop" style="background:linear-gradient(#e8eef2,#6aa33a)"></span>
      <span role="img" aria-label="Gallery photo of a customer" style="background:linear-gradient(#c9a37e,#7a5a3c)"></span>
      <span role="img" aria-label="Gallery photo of a green landscape" style="background:linear-gradient(#3f7d3a,#9fc04a)"></span>
      <span role="img" aria-label="Gallery photo of grass" style="background:linear-gradient(#f2f6e6,#6fb52c)"></span>
      <span role="img" aria-label="Gallery photo of foliage" style="background:linear-gradient(#9dbb4a,#4c6e22)"></span>
      <span role="img" aria-label="Gallery photo of a family outdoors" style="background:linear-gradient(#a7c46a,#b48a6a)"></span>
    </div>
    <a class="btn" href="#" style="position:absolute;left:69px;top:118px;padding:5px 4px">more gallery</a>
  </div>
  <div class="abs footer-col" style="left:674px">
    <h5>GET IN TOUCH</h5>
    <div class="map-area" role="img" aria-label="Street map showing the office location"></div>
    <p style="margin-top:8px;font-size:6px;line-height:10px">14 Fernbrook Lane<br>ASHVALE, WA 6000</p>
    <div class="contact-line"><i></i>08 5550 2288</div>
    <div class="contact-line"><i></i>08 5550 2288</div>
    <div class="contact-line" style="color:#8a8a8a"><i></i>info@hollowridge.example</div>
  </div>
</footer>

<div class="abs base-bar">
  <p>© 2013 Hollow Ridge Branchworks.</p>
  <div class="social"><span></span><span></span><span></span></div>
</div>

</body>
</html>
```